FixyFellas,com Home Maintenance Membership Website

Fixy Fellas is a yearly home maintenance membership website where Home Owners, Contractor, and Subcontractors can interact in an online bidding environment to exchange goods and services.

Our Tag Line Is: We Tackle The Weekend Lists That Other Fellas Won't Tackle
Updates

Target Market(s)

Homeowner, Female, 26 to 56 years of age. Middle to upper income.
Contractors/Subcontractors

Industry/Entity Type

Environment

Font styles to use
Other font styles liked:
• We want to match the logo font

Requirements
Must have
• Three-tiered membership plans for homeowners. Features and pricing TBD
Three major customer components as well as a administration back end. The three main components will be Home Owners Page, Contractors/Subcontractors pages, and the request-for Work Pages.
Need Membership levels panel similar to the uploaded picture
We did like this site as a start point. http://www.coatguardprime.example/
Nice to have
• #1: Customer domain profiles for contractors
#2: Blog
#3: Affiliate Program
#4: Contractor Rating System
#5: Internal Messaging System
#6: Banner Ads
#7: Escrow Payments

```html
<!DOCTYPE html>
<html lang="en">
<head>
<meta charset="utf-8">
<title>Fixy Fellas – Home Maintenance Membership</title>
<link rel="stylesheet" href="https://fonts.googleapis.com/css2?family=Open+Sans:ital,wght@0,400;0,600;0,700;1,600&family=PT+Serif&display=swap">
<style>
:root{
  --orange:#e2500b;
  --orange-light:#f5711f;
  --ink:#1a1a1a;
  --text:#333;
  --muted:#555;
  --panel:#efefef;
  --black:#050505;
  --nav:#2b2b2b;
  --white:#fff;
  --cyan:#4fc3f7;
}
*{box-sizing:border-box;margin:0;padding:0}
html,body{width:1200px;height:2439px;overflow:hidden;background:var(--white)}
body{position:relative;font-family:"Open Sans",Arial,sans-serif;color:var(--text)}
.abs{position:absolute}

/* header */
.brand-mark{left:120px;top:22px;width:110px;height:110px;border-radius:50%;background:var(--ink)}
.brand-name{left:240px;top:62px;font-size:24px;font-weight:700;color:var(--orange)}
.member-links{right:122px;top:14px;font-size:12px;color:var(--orange);letter-spacing:.3px}
.main-nav{left:359px;top:47px;width:721px;height:55px;border-radius:4px;background:linear-gradient(#3a3a3a,#1c1c1c);display:flex;align-items:center;padding:0 24px;box-shadow:0 1px 3px rgba(0,0,0,.4)}
.main-nav a{color:var(--white);text-decoration:none;font-size:13px;margin-right:30px}
.search{margin-left:auto;width:190px;height:28px;border-radius:14px;background:#111;color:#ccc;font-size:11px;display:flex;align-items:center;justify-content:space-between;padding:0 12px}

/* hero */
.hero-photo{left:119px;top:125px;width:961px;height:351px;background:linear-gradient(135deg,#dfe5ea 0%,#a9b7c3 35%,#7d8f9c 60%,#8d6e55 85%,#5d4a3a 100%)}
.welcome{left:119px;top:476px;width:961px;height:174px;background:var(--orange);color:var(--white);text-align:center;padding:22px 60px 0}
.welcome h1{font-size:24px;font-weight:400;margin-bottom:18px}
.welcome p{font-size:12px;line-height:21px}

/* section titles */
.section-title{left:0;width:1200px;text-align:center;font-size:24px;font-weight:400;color:var(--ink)}

/* affiliate */
.feature{width:260px;text-align:center}
.feature-icon{width:68px;height:68px;margin:0 auto 18px;border-radius:8px;background:#1a1a1a;display:flex;align-items:center;justify-content:center}
.feature h3{font-size:16px;font-weight:600;color:var(--orange);margin-bottom:4px}
.feature p{font-size:12px;line-height:23px;color:var(--text)}

/* membership */
.plans-panel{left:119px;top:1000px;width:961px;height:512px;background:var(--panel)}
.plan{background:var(--white)}
.plan-head{height:35px;background:var(--black);color:var(--white);font-size:16px;padding:7px 15px}
.plan-price{height:116px;background:linear-gradient(#7a7a7a,#1e1e1e);color:var(--white);display:flex;align-items:center;justify-content:center;font-family:"PT Serif",Georgia,serif;font-size:52px}
.plan-price small{font-family:"Open Sans",Arial,sans-serif;font-size:15px;margin:20px 0 0 4px}
.plan ul{list-style:none;padding:16px 0 0 14px}
.plan li{font-size:12.5px;font-weight:600;color:var(--ink);height:34px;white-space:nowrap}
.plan li::before{content:"›";font-weight:700;margin-right:7px;font-size:15px}
.plan-btn{position:absolute;left:50%;transform:translateX(-50%);bottom:-10px;width:103px;height:31px;border-radius:3px;background:var(--black);color:var(--white);font-size:12px;font-weight:600;display:flex;align-items:center;justify-content:center}
.plan.featured{box-shadow:0 0 10px rgba(0,0,0,.55);z-index:2}
.plan.featured .plan-head{background:var(--orange)}
.plan.featured .plan-price{background:linear-gradient(var(--orange-light),var(--orange))}
.plan.featured .plan-btn{background:var(--orange-light)}

/* rating */
.rating{width:280px}
.rating h4{font-size:14px;font-weight:600;color:var(--ink);margin-bottom:8px}
.rating p{font-size:12px;line-height:22px;color:var(--text);margin-bottom:6px}
.stars{display:flex;gap:4px;margin-bottom:6px}
.see-list{font-size:13px;font-weight:700;color:var(--orange)}
.divider{left:119px;top:1799px;width:961px;height:2px;background:#bbb}

/* blog */
.blog-title{left:117px;top:1830px;font-size:24px;color:var(--ink)}
.post-photo{width:137px;height:125px;background:linear-gradient(135deg,#b07a4f,#7d5a3e 50%,#d8c9b5)}
.post{width:330px}
.post time{display:block;font-size:15px;color:var(--orange);margin-bottom:12px}
.post h5{font-size:16px;font-weight:400;color:var(--ink);line-height:22px;margin-bottom:8px}
.post p{font-size:11.5px;line-height:22px;color:var(--text)}

/* banner */
.banner{left:748px;top:1834px;width:332px;height:366px;border-radius:5px;overflow:hidden;display:grid;grid-template-columns:1fr 1fr;grid-template-rows:1fr 1fr;gap:2px;background:#222}
.banner-cell{position:relative}
.banner-cell.a{background:linear-gradient(160deg,#2f4f7c,#7b8fa3 55%,#3b3b3b)}
.banner-cell.b{background:linear-gradient(160deg,#5f7f3b,#8a4a3a 55%,#4b3b2b)}
.banner-cell.c{background:linear-gradient(160deg,#c8d4de,#8e9aa3 55%,#4d5a3d)}
.banner-cell.d{background:linear-gradient(160deg,#b9d6ea,#c87b7b 55%,#5a6d3e)}
.banner-caption{position:absolute;left:0;right:0;bottom:0;height:50px;background:rgba(0,0,0,.7);padding:6px 4px;font-size:11px;line-height:19px;color:var(--white);font-weight:600;white-space:nowrap;overflow:hidden}
.banner-caption span{display:block;color:var(--cyan)}
.banner-label{left:760px;top:2098px;font-size:28px;font-style:italic;font-weight:600;color:var(--white);z-index:3}

/* footer */
.site-footer{left:0;top:2252px;width:1200px;height:187px;background:var(--black);color:var(--white)}
.social{display:flex;gap:8px;position:absolute;left:356px;top:27px}
.social span{width:37px;height:37px;border-radius:50%;background:var(--white)}
.cards{display:flex;gap:6px;position:absolute;left:498px;top:32px}
.cards span{width:50px;height:28px;border-radius:3px;background:#e8e8e8}
.footer-links{position:absolute;left:0;width:1200px;top:86px;text-align:center;font-size:12.5px;font-weight:600}
.footer-rule{position:absolute;left:119px;top:125px;width:961px;height:1px;background:#333}
.copyright{position:absolute;left:0;width:1200px;top:142px;text-align:center;font-size:12px;color:#555}
</style>
</head>
<body>

<header>
  <div class="abs brand-mark"></div>
  <div class="abs brand-name">Fixy Fellas</div>
  <div class="abs member-links">MEMBER LOGIN &nbsp;|&nbsp; SIGN UP</div>
  <nav class="abs main-nav">
    <a href="#">HOME</a><a href="#">ABOUT US</a><a href="#">SERVICES</a><a href="#">BLOG</a><a href="#">CONTACT US</a>
    <div class="search">Search
      <svg width="11" height="11" viewBox="0 0 12 12"><circle cx="5" cy="5" r="3.6" fill="none" stroke="#ccc" stroke-width="1.6"/><line x1="7.6" y1="7.6" x2="11" y2="11" stroke="#ccc" stroke-width="1.8"/></svg>
    </div>
  </nav>
</header>

<div class="abs hero-photo" role="img" aria-label="Photo of a man pressure-washing the wooden deck of a house"></div>
<section class="abs welcome">
  <h1>WELCOME TO FIXY FELLAS</h1>
  <p>Proin gravida nibh vel velit auctor aliquet. Aenean sollicitudin, lorem quis bibendum auctor, nisi elit consequat ipsum, nec sagittis sem nibh id elit. Duis sed odio sit amet nibh vulputate cursus a sit amet mauris. Morbi accumsan ipsum velit. Nam nec tellus a odio tincidunt auctor a ornare odio. Sed non &nbsp;mauris vitae erat consequat auctor eu in elit. Class aptent taciti sociosqu ad litora torquent per conubia nostra, per inceptos himenaeos.</p>
</section>

<h2 class="abs section-title" style="top:700px">AFFILIATE PROGRAM</h2>
<div class="abs feature" style="left:155px;top:785px">
  <div class="feature-icon"><svg width="40" height="40" viewBox="0 0 40 40" fill="none" stroke="#fff" stroke-width="3" stroke-linejoin="round"><path d="M8 20 L20 9 L32 20"/><path d="M13 18 V28 H27 V18"/><path d="M4 26 Q10 36 20 35 Q30 36 36 26"/></svg></div>
  <h3>Proin Gravida Nibh Velvelit</h3>
  <p>Lorem psum proin gravida nibh vel<br>velit auctor aliquetsollicitudin</p>
</div>
<div class="abs feature" style="left:480px;top:785px">
  <div class="feature-icon"><svg width="40" height="40" viewBox="0 0 40 40" stroke="#fff" stroke-width="4" stroke-linecap="round"><line x1="9" y1="31" x2="31" y2="9"/><line x1="9" y1="9" x2="31" y2="31"/><circle cx="30" cy="10" r="5" fill="none" stroke-width="3"/></svg></div>
  <h3>Proin Gravida Nibh Velvelit</h3>
  <p>Lorem psum proin gravida nibh vel<br>velit auctor aliquetsollicitudin</p>
</div>
<div class="abs feature" style="left:822px;top:785px">
  <div class="feature-icon"><svg width="40" height="40" viewBox="0 0 40 40" fill="none" stroke="#fff" stroke-width="3" stroke-linejoin="round"><path d="M5 21 L20 8 L35 21"/><path d="M10 18 V32 H30 V18"/><rect x="17" y="23" width="6" height="9" fill="#fff"/></svg></div>
  <h3>Proin Gravida Nibh Velvelit</h3>
  <p>Lorem psum proin gravida nibh vel<br>velit auctor aliquetsollicitudin</p>
</div>

<section class="abs plans-panel"></section>
<h2 class="abs section-title" style="top:1020px">MEMBERSHIP PLANS</h2>

<div class="abs plan" style="left:312px;top:1093px;width:199px;height:374px">
  <div class="plan-head">PLAN 1</div>
  <div class="plan-price">$30<small>MO</small></div>
  <ul><li>Proin gravida nibh vel velit</li><li>Aenean sollicitudin lorem</li><li>Duis bibendum auctornisi</li><li>Sagittis sem nibh id elited</li><li>Da odio tincidunt auctor a</li></ul>
  <div class="plan-btn">SING UP</div>
</div>
<div class="abs plan featured" style="left:511px;top:1088px;width:191px;height:384px">
  <div class="plan-head" style="height:40px;padding-top:10px">PLAN 3</div>
  <div class="plan-price">$90<small>MO</small></div>
  <ul><li>Proin gravida nibh vel velit</li><li>Aenean sollicitudin lorem</li><li>Duis bibendum auctornisi</li><li>Sagittis sem nibh id elited</li><li>Da odio tincidunt auctor a</li></ul>
  <div class="plan-btn" style="bottom:-5px">SING UP</div>
</div>
<div class="abs plan" style="left:702px;top:1093px;width:197px;height:374px">
  <div class="plan-head">PLAN 1</div>
  <div class="plan-price">$50<small>MO</small></div>
  <ul><li>Proin gravida nibh vel velit</li><li>Aenean sollicitudin lorem</li><li>Duis bibendum auctornisi</li><li>Sagittis sem nibh id elited</li><li>Da odio tincidunt auctor a</li></ul>
  <div class="plan-btn">SING UP</div>
</div>

<h2 class="abs section-title" style="top:1560px">CONTRACTOR RATING</h2>
<div class="abs rating" style="left:122px;top:1628px">
  <h4>Lorem quis bibendum auctor</h4>
  <p>Lorem psum proin gravida nibh vel velit auctor aliquetsollicitudin gravida nibh auctor aliquet.</p>
  <div class="stars"><svg width="88" height="16" viewBox="0 0 88 16" fill="#e2500b"><g id="star"><polygon points="8,0 10,5.5 16,6 11.5,9.8 13,16 8,12.6 3,16 4.5,9.8 0,6 6,5.5"/></g><use href="#star" x="22"/><use href="#star" x="44"/><use href="#star" x="66"/></svg></div>
  <div class="see-list">See List &raquo;</div>
</div>
<div class="abs rating" style="left:460px;top:1628px">
  <h4>Lorem quis bibendum auctor</h4>
  <p>Lorem psum proin gravida nibh vel velit auctor aliquetsollicitudin gravida nibh auctor aliquet.</p>
  <div class="stars"><svg width="88" height="16" viewBox="0 0 88 16" fill="#e2500b"><use href="#star"/><use href="#star" x="22"/><use href="#star" x="44"/><use href="#star" x="66"/></svg></div>
  <div class="see-list">See List &raquo;</div>
</div>
<div class="abs rating" style="left:810px;top:1628px">
  <h4>Lorem quis bibendum auctor</h4>
  <p>Lorem psum proin gravida nibh vel velit auctor aliquetsollicitudin gravida nibh auctor aliquet.</p>
  <div class="stars"><svg width="88" height="16" viewBox="0 0 88 16" fill="#e2500b"><use href="#star"/><use href="#star" x="22"/><use href="#star" x="44"/><use href="#star" x="66"/></svg></div>
  <div class="see-list">See List &raquo;</div>
</div>

<div class="abs divider"></div>

<h2 class="abs blog-title">BLOG</h2>
<div class="abs post-photo" style="left:119px;top:1888px" role="img" aria-label="Photo of two workers building wooden cabinets"></div>
<article class="abs post" style="left:268px;top:1882px">
  <time>15 Nov 2014</time>
  <h5>Proin gravida nibh vel velit auctor aliquet<br>lorem quis bibendum auctor, nisi elit</h5>
  <p>Lorem quis bibendum auctor, nisi elit onsequat ipsum<br>nec sagittis sem nibh id elit. Duis sed odio sit amet</p>
</article>
<div class="abs post-photo" style="left:119px;top:2073px" role="img" aria-label="Photo of a worker carrying a cardboard box"></div>
<article class="abs post" style="left:268px;top:2067px">
  <time>15 Nov 2014</time>
  <h5>Proin gravida nibh vel velit auctor aliquet<br>lorem quis bibendum auctor, nisi elit</h5>
  <p>Lorem quis bibendum auctor, nisi elit onsequat ipsum<br>nec sagittis sem nibh id elit. Duis sed odio sit amet</p>
</article>

<aside class="abs banner">
  <div class="banner-cell a" role="img" aria-label="Photo of a modern house at dusk"><div class="banner-caption">Harlow Point, West Bay<span>Sleeps 16 | Bedrooms 8</span></div></div>
  <div class="banner-cell b" role="img" aria-label="Photo of an ivy-covered brick house"><div class="banner-caption">Harlow Point, West Bay<span>Sleeps 16 | Bedrooms 8</span></div></div>
  <div class="banner-cell c" role="img" aria-label="Photo of a white cottage"><div class="banner-caption">Harlow Point, West Bay<span>Sleeps 16 | Bedrooms 8</span></div></div>
  <div class="banner-cell d" role="img" aria-label="Photo of a pink seaside house"><div class="banner-caption">Harlow Point, West Bay<span>Sleeps 16 | Bedrooms 8</span></div></div>
</aside>
<div class="abs banner-label">Place for Banner Ads</div>

<footer class="abs site-footer">
  <div class="social"><span></span><span></span><span></span></div>
  <div class="cards"><span></span><span></span><span></span><span></span><span></span><span></span><span></span></div>
  <div class="footer-links">Company &nbsp;|&nbsp; Products &nbsp;|&nbsp; Support &nbsp;|&nbsp; Affiliate &nbsp;|&nbsp; Contractor &nbsp;|&nbsp; Home Owners &nbsp;|&nbsp; Contact Us &nbsp;|&nbsp; Privacy Statement &nbsp;|&nbsp; Site Map</div>
  <div class="footer-rule"></div>
  <div class="copyright">Copyright © 2014 All rights reserved</div>
</footer>

</body>
</html>
```